Riverstone & Pine Construction and Developments business cards

A business card with watermark background (construction work)

Company logo attached

Home improvement projects
House renovations
Bathroom and kitchen renovations
House extensions
New builds and granny flats

Director Omar Haddine
(Phone number)
omar@rpcbuildgroup.com.au
(Instagram logo) rpc_buildgroup

```html
<!DOCTYPE html>
<html lang="en">
<head>
<meta charset="utf-8">
<title>Riverstone &amp; Pine Construction and Developments – Business Cards</title>
<link rel="stylesheet" href="https://fonts.googleapis.com/css2?family=Montserrat:wght@600;700&family=Arimo:wght@400;700&display=swap">
<style>
  :root {
    --brand-blue: #2169b2;
    --ink: #1b1b1b;
    --paper: #ffffff;
    --backdrop: #e4e5e7;
    --text-light: #ffffff;
  }
  * { box-sizing: border-box; margin: 0; padding: 0; }
  html, body { width: 1200px; height: 800px; overflow: hidden; }
  body {
    background: var(--backdrop);
    display: flex;
    align-items: center;
    justify-content: center;
    gap: 40px;
    font-family: "Arimo", Arial, sans-serif;
  }
  .card {
    position: relative;
    width: 540px;
    height: 310px;
    border-radius: 18px;
    overflow: hidden;
    box-shadow: 0 10px 28px rgba(0,0,0,0.22);
  }

  /* Contact side */
  .card--contact { background: var(--brand-blue); }
  .contact__brand-panel {
    position: absolute;
    inset: 0 auto 0 0;
    width: 212px;
    background: var(--paper);
    display: flex;
    align-items: center;
    justify-content: center;
    padding: 0 22px;
  }
  .contact__divider {
    position: absolute;
    left: 200px;
    top: 0;
    width: 30px;
    height: 310px;
  }
  .brand-name {
    font-family: "Montserrat", Arial, sans-serif;
    font-weight: 700;
    line-height: 1.15;
    display: flex;
    align-items: center;
    gap: 10px;
  }
  .brand-name__mark {
    flex: none;
    width: 12px;
    height: 12px;
  }
  .brand-name--small { color: var(--brand-blue); font-size: 15px; }
  .brand-name--small .brand-name__mark { background: var(--brand-blue); }
  .brand-name--large { color: var(--text-light); font-size: 26px; }
  .brand-name--large .brand-name__mark { background: var(--text-light); width: 16px; height: 16px; }

  .contact__details {
    position: absolute;
    left: 262px;
    top: 62px;
    color: var(--text-light);
  }
  .person__name {
    font-family: "Montserrat", Arial, sans-serif;
    font-weight: 700;
    font-size: 22px;
    letter-spacing: 0.5px;
    text-transform: uppercase;
  }
  .person__title { font-size: 14px; margin-top: 2px; }
  .contact-list { list-style: none; margin-top: 26px; }
  .contact-list__item {
    display: flex;
    align-items: center;
    gap: 9px;
    font-size: 13.5px;
    line-height: 22px;
  }
  .contact-list__icon { width: 12px; height: 12px; flex: none; }
  .contact-list__dot {
    width: 10px; height: 10px; border-radius: 50%;
    border: 1.5px solid var(--text-light); flex: none; margin: 0 1px;
  }

  /* Front side */
  .card--front {
    background: var(--brand-blue);
    color: var(--text-light);
    display: flex;
    flex-direction: column;
    align-items: center;
    justify-content: center;
    padding: 0 34px;
    text-align: center;
  }
  .front__brand { max-width: 400px; margin-top: 10px; }
  .services {
    margin-top: 56px;
    font-size: 13.5px;
    line-height: 19px;
  }
  .services__sep { font-weight: 700; margin: 0 4px; }
</style>
</head>
<body>

  <section class="card card--contact" aria-label="Business card, contact side">
    <div class="contact__brand-panel">
      <p class="brand-name brand-name--small">
        <span class="brand-name__mark" aria-hidden="true"></span>
        <span>Riverstone &amp; Pine Construction and Developments</span>
      </p>
    </div>
    <svg class="contact__divider" viewBox="0 0 30 310" aria-hidden="true">
      <polyline points="12,0 12,130 22,138 17,142 12,150 12,310" fill="none" stroke="#1b1b1b" stroke-width="2.5"/>
    </svg>

    <div class="contact__details">
      <h1 class="person__name">Omar Haddine</h1>
      <p class="person__title">Director</p>
      <ul class="contact-list">
        <li class="contact-list__item">
          <svg class="contact-list__icon" viewBox="0 0 24 24" aria-hidden="true"><path fill="#fff" d="M6.6 10.8a15.1 15.1 0 0 0 6.6 6.6l2.2-2.2a1 1 0 0 1 1-.25 11.4 11.4 0 0 0 3.6.57 1 1 0 0 1 1 1V20a1 1 0 0 1-1 1A17 17 0 0 1 3 4a1 1 0 0 1 1-1h3.5a1 1 0 0 1 1 1c0 1.25.2 2.45.57 3.57a1 1 0 0 1-.25 1z"/></svg>
          <span>369-482-1750</span>
        </li>
        <li class="contact-list__item">
          <svg class="contact-list__icon" viewBox="0 0 24 24" aria-hidden="true"><rect x="2" y="5" width="20" height="14" rx="1.5" fill="#fff"/><polyline points="3,6 12,13 21,6" fill="none" stroke="#2169b2" stroke-width="2"/></svg>
          <span>omar@rpcbuildgroup.com.au</span>
        </li>
        <li class="contact-list__item">
          <svg class="contact-list__icon" viewBox="0 0 24 24" aria-hidden="true"><circle cx="12" cy="12" r="10" fill="#fff"/><path d="M2 12h20M12 2c3 3 3 17 0 20M12 2c-3 3-3 17 0 20" fill="none" stroke="#2169b2" stroke-width="1.6"/></svg>
          <span>rpcbuildgroup.com.au</span>
        </li>
        <li class="contact-list__item">
          <span class="contact-list__dot" aria-hidden="true"></span>
          <span>rpc_buildgroup</span>
        </li>
      </ul>
    </div>
  </section>

  <section class="card card--front" aria-label="Business card, front side">
    <p class="brand-name brand-name--large front__brand">
      <span class="brand-name__mark" aria-hidden="true"></span>
      <span>Riverstone &amp; Pine Construction and Developments</span>
    </p>
    <p class="services">
      Home improvement projects<span class="services__sep">::</span>House renovations<span class="services__sep">::</span>House extensions<br>
      Bathroom &amp; kitchen renovations<span class="services__sep">::</span>New builds &amp; granny flats
    </p>
  </section>

</body>
</html>
```